Harborline Building Partners
Owner's Rep
Professional
Daniel Marsh
Wrenhaven Island Marlow County
dan@harborlnbuildingpartners.com
www.harborlnbuildingpartners.com
Your advocate for your construction needs
* New Construction * Remolding Projects * Maintenance and Service work * Off-season and pre-season inspections

```html
<!DOCTYPE html>
<html lang="en">
<head>
<meta charset="utf-8">
<title>Harborline Building Partners – Business Card</title>
<link href="https://fonts.googleapis.com/css2?family=Libre+Baskerville:wght@400;700&family=Open+Sans:wght@400;600&display=swap" rel="stylesheet">
<style>
  :root {
    --bg: #1f1f22;
    --sky: #35bdee;
    --navy: #1e2f58;
    --ink: #2a3550;
    --muted: #7a8190;
    --paper: #ffffff;
    --rule: #c9cdd5;
  }
  html, body {
    margin: 0;
    padding: 0;
    width: 1200px;
    height: 871px;
    overflow: hidden;
    background: var(--bg);
  }
  .stage {
    position: relative;
    width: 1200px;
    height: 871px;
  }
  .card {
    position: absolute;
    width: 560px;
    height: 320px;
    border-radius: 3px;
    overflow: hidden;
    box-sizing: border-box;
  }

  /* Front */
  .card-front {
    left: 60px;
    top: 90px;
    background: var(--sky);
    color: var(--paper);
    display: flex;
    flex-direction: column;
    align-items: center;
    justify-content: center;
    padding-bottom: 30px;
  }
  .front-mark {
    width: 22px;
    height: 22px;
    border-radius: 50%;
    background: var(--paper);
    margin-bottom: 14px;
  }
  .front-name {
    font-family: "Libre Baskerville", serif;
    font-weight: 700;
    font-size: 26px;
    letter-spacing: 1px;
    text-transform: uppercase;
    text-align: center;
    line-height: 1.3;
  }
  .front-slogan {
    font-family: "Open Sans", sans-serif;
    font-size: 12px;
    margin-top: 12px;
    letter-spacing: 0.5px;
  }
  .front-services {
    position: absolute;
    left: 0;
    right: 0;
    bottom: 22px;
    text-align: center;
    font-family: "Open Sans", sans-serif;
    font-size: 9.5px;
    letter-spacing: 0.2px;
    white-space: nowrap;
  }

  /* Back */
  .card-back {
    left: 580px;
    top: 461px;
    background: var(--paper);
  }
  .back-logo {
    position: absolute;
    left: 28px;
    top: 122px;
    width: 240px;
    display: flex;
    align-items: center;
    gap: 10px;
  }
  .back-mark {
    flex: 0 0 18px;
    height: 18px;
    border-radius: 50%;
    background: var(--sky);
  }
  .back-name {
    font-family: "Libre Baskerville", serif;
    font-weight: 700;
    font-size: 16px;
    color: var(--navy);
    text-transform: uppercase;
    line-height: 1.35;
    white-space: nowrap;
  }
  .divider {
    position: absolute;
    left: 275px;
    top: 34px;
    width: 1px;
    height: 196px;
    background: var(--rule);
  }
  .details {
    position: absolute;
    left: 295px;
    top: 36px;
    right: 16px;
  }
  .person {
    font-family: "Libre Baskerville", serif;
    font-weight: 700;
    font-size: 21px;
    color: var(--navy);
    text-transform: uppercase;
    letter-spacing: 0.5px;
    margin: 0;
  }
  .role {
    font-family: "Open Sans", sans-serif;
    font-size: 11px;
    color: var(--muted);
    margin: 4px 0 22px;
  }
  .place {
    font-family: "Open Sans", sans-serif;
    font-size: 11px;
    color: var(--ink);
    line-height: 1.45;
    margin: 0 0 18px;
  }
  .contacts {
    list-style: none;
    margin: 0;
    padding: 0;
  }
  .contacts li {
    display: flex;
    align-items: center;
    gap: 8px;
    font-family: "Open Sans", sans-serif;
    font-size: 11px;
    color: var(--ink);
    margin-bottom: 5px;
    white-space: nowrap;
  }
  .contacts svg {
    flex: 0 0 12px;
  }
  .footer-band {
    position: absolute;
    left: 0;
    bottom: 0;
    width: 560px;
    height: 34px;
  }
</style>
</head>
<body>
<main class="stage">

  <section class="card card-front" aria-label="Business card front">
    <div class="front-mark"></div>
    <div class="front-name">Harborline<br>Building Partners</div>
    <div class="front-slogan">Your advocate for your construction needs</div>
    <div class="front-services">New Construction • Remolding Projects • Maintenance and Service work • Off-season and pre-season inspections</div>
  </section>

  <section class="card card-back" aria-label="Business card back">
    <div class="back-logo">
      <span class="back-mark"></span>
      <span class="back-name">Harborline<br>Building Partners</span>
    </div>

    <div class="divider"></div>

    <div class="details">
      <h1 class="person">Daniel Marsh</h1>
      <p class="role">Owner's Rep</p>
      <p class="place">Wrenhaven<br>Island Marlow County</p>
      <ul class="contacts">
        <li>
          <svg width="12" height="12" viewBox="0 0 12 12" aria-hidden="true">
            <circle cx="6" cy="6" r="6" fill="var(--sky)"/>
            <path d="M4 3.2 L5 4.6 L4.5 5.3 Q5.3 6.8 6.7 7.5 L7.4 7 L8.8 8 L8.2 9 Q5.6 8.9 3.2 4 Z" fill="#fff"/>
          </svg>
          609-555-0147
        </li>
        <li>
          <svg width="12" height="12" viewBox="0 0 12 12" aria-hidden="true">
            <circle cx="6" cy="6" r="6" fill="var(--sky)"/>
            <rect x="3" y="4" width="6" height="4.2" fill="#fff"/>
            <path d="M3 4 L6 6.3 L9 4" stroke="var(--sky)" stroke-width="0.7" fill="none"/>
          </svg>
          dan@harborlnbuildingpartners.com
        </li>
        <li>
          <svg width="12" height="12" viewBox="0 0 12 12" aria-hidden="true">
            <circle cx="6" cy="6" r="6" fill="var(--sky)"/>
            <circle cx="6" cy="6" r="3" fill="none" stroke="#fff" stroke-width="0.8"/>
            <path d="M3 6 H9 M6 3 Q4.5 6 6 9 M6 3 Q7.5 6 6 9" stroke="#fff" stroke-width="0.6" fill="none"/>
          </svg>
          www.harborlnbuildingpartners.com
        </li>
      </ul>
    </div>

    <svg class="footer-band" viewBox="0 0 560 34" aria-hidden="true">
      <rect x="0" y="16" width="560" height="18" fill="var(--navy)"/>
      <polygon points="470,0 560,0 560,16 452,16" fill="var(--sky)"/>
    </svg>
  </section>

</main>
</body>
</html>
```